Digital Menu for New Picnic Company

We're in the process of creating a new picnic business called Fernvale Hampers. We need our menu created as per the content in this google doc https://files.quorvex.net/doc/7Kq2Lm9XpR4tWz8BnC3vYh6JdS5gFa1eTu0iOo/view?share=open
Please look at our website www.fernvalehampers.com.au to get an understanding of what we do and our branding style. We need the menu to be created matching the branding/colours as per our website however other than that please feel free to design it however you like and I will provide feedback from there. We are offering a high end gourmet product so the look and feel of the menu does need to reflect this.
PLEASE NOTE: This menu will only be displayed online as a PDF and doesn't need to be printed or provided physically.

```html
<!DOCTYPE html>
<html lang="en">
<head>
<meta charset="utf-8">
<title>Fernvale Hampers – Gourmet Picnic Menu</title>
<link rel="stylesheet" href="https://fonts.googleapis.com/css2?family=Abril+Fatface&family=Montserrat:ital,wght@0,400;0,600;0,700;1,700&display=swap">
<style>
:root{
  --bg:#1c1c1c;
  --paper:#f4f4f2;
  --card:#ffffff;
  --green:#5cbb46;
  --ink:#1a1a1a;
  --blue:#1b9fe0;
  --white:#ffffff;
}
*{margin:0;padding:0;box-sizing:border-box}
html,body{width:1200px;height:800px;overflow:hidden}
body{background:var(--bg);font-family:"Montserrat",sans-serif;color:var(--ink);position:relative}
.page{position:absolute;background:var(--paper);overflow:hidden}
.photo{position:absolute;z-index:0}
.ribbon{position:absolute;background:var(--green);color:var(--white);font-weight:700;display:flex;align-items:center;justify-content:center;letter-spacing:.3px;
  clip-path:polygon(0 0,100% 0,94% 50%,100% 100%,0 100%,6% 50%);white-space:nowrap;z-index:2}
.ribbon::before,.ribbon::after{content:"•";margin:0 .5em;font-weight:700}
.choose{position:absolute;z-index:3;border-radius:50%;background:var(--blue);color:var(--white);font-style:italic;font-weight:700;display:flex;flex-direction:column;align-items:center;justify-content:center;line-height:1;border:1.5px solid var(--white)}
.choose small{font-size:.7em;font-weight:600}
.list{position:absolute;z-index:2;list-style:none;font-size:4.6px;font-weight:700;line-height:7.6px;letter-spacing:-.05px;white-space:nowrap}
.list li::before{content:"";display:inline-block;width:2.4px;height:2.4px;border-radius:50%;background:var(--green);margin-right:3px;vertical-align:middle}
.head{position:absolute;z-index:2;font-size:6.5px;font-weight:700;letter-spacing:.3px}

/* cover */
.cover{left:124px;top:50px;width:496px;height:701px}
.cover-card{position:absolute;left:42px;top:35px;width:411px;height:610px;background:var(--card);z-index:1}
.brand-name{position:absolute;left:0;width:100%;top:97px;text-align:center;color:var(--green);font-weight:700;font-size:20px;z-index:3;display:flex;align-items:center;justify-content:center;gap:7px}
.brand-name .dot{width:10px;height:10px;border-radius:50%;background:var(--green)}
.title{position:absolute;left:0;width:100%;top:178px;text-align:center;font-family:"Abril Fatface",serif;font-size:66px;line-height:1;letter-spacing:-1px;z-index:3}
.cover .ribbon{left:129px;top:251px;width:237px;height:32px;font-size:20px;font-weight:400;z-index:3}
.intro{position:absolute;left:72px;width:350px;text-align:center;font-size:10.4px;line-height:14.2px;z-index:3}
.intro .hl{color:var(--green);font-weight:700}
.divider{position:absolute;left:116px;top:572px;width:266px;height:10px;z-index:3}
.url{position:absolute;left:0;width:100%;top:605px;text-align:center;color:var(--green);font-weight:700;font-size:10px;z-index:3}

.p2{left:657px;top:48px;width:238px;height:337px}
.p3{left:920px;top:48px;width:238px;height:337px}
.p4{left:657px;top:412px;width:238px;height:338px}
.sm{height:14px;font-size:8.5px}

.side-brand{position:absolute;left:940px;top:585px;width:210px;text-align:center;color:var(--green);font-weight:700;font-size:20px;white-space:nowrap;display:flex;align-items:center;justify-content:center;gap:8px}
.side-brand .dot{width:11px;height:11px;border-radius:50%;background:var(--green)}
</style>
</head>
<body>

<section class="page cover">
  <div class="photo" role="img" aria-label="Wedges of cheese with basil on a wooden board" style="left:335px;top:20px;width:161px;height:240px;background:linear-gradient(135deg,#c99a5a,#f4dd8a 55%,#e9c667);border-radius:14px 0 0 14px;z-index:2"></div>
  <div class="photo" role="img" aria-label="Sliced red chillies" style="left:0;top:555px;width:42px;height:90px;background:linear-gradient(#f1e9e6,#d8452f 60%,#f1e9e6)"></div>
  <div class="photo" role="img" aria-label="Bowls of guacamole and corn chips" style="left:0;top:645px;width:496px;height:56px;background:linear-gradient(90deg,#a6a25a,#c8c07a 40%,#f0d48a 60%,#e9c068)"></div>
  <div class="cover-card"></div>
  <div class="brand-name"><span class="dot"></span>Fernvale Hampers</div>
  <h1 class="title">GOURMET</h1>
  <div class="ribbon">PICNIC MENU</div>
  <p class="intro" style="top:315px">Our Gourmet Picnics are handcrafted and delivered to your picnic spot on a wooden grazing tray. They come sealed in a catering box to ensure they are not tampered with. You then open the box and remove the grazing tray to enjoy the food. We prepare our food in accordance with food handling guidelines and all <span class="hl">COVID</span>precautions.</p>
  <p class="intro" style="top:414px">We also provide complimentary beverages as part of the Gourmet Picnic being your choice of beers, wine or soft drink. You also can choose between still or sparkling water.</p>
  <p class="intro" style="top:470px">As everyone has varying tastes, we have created our menu to be fully customisable so you can design your own picnic. We offer a wide variety of choices while focussing on quality ingredients for each component of your picnic.</p>
  <svg class="divider" viewBox="0 0 266 10"><path d="M4 5 H262" stroke="#1a1a1a" stroke-width="1" fill="none"/></svg>
  <div class="url">fernvalehampers.com.au</div>
</section>

<section class="page p2">
  <div class="photo" role="img" aria-label="Blue vein cheese and a bowl of red dip" style="left:0;top:20px;width:90px;height:100px;background:linear-gradient(135deg,#e8ecef,#b9c6cf 50%,#b33b22);border-radius:8px"></div>
  <div class="choose" style="left:37px;top:81px;width:32px;height:32px;font-size:7px">Choose<small>any 2</small></div>
  <div class="ribbon sm" style="left:101px;top:19px;width:112px">CHEESE &amp; DIPS</div>
  <div class="head" style="left:102px;top:46px">CHEESES</div>
  <div class="head" style="left:162px;top:46px">DIPS</div>
  <ul class="list" style="left:101px;top:59px"><li>Creamy Blue</li><li>Blue Vein</li><li>Chilli Cream</li><li>Double Cream Brie</li><li>Camembert</li><li>Cheddar</li><li>Vintage Cheddar</li><li>Parmesan</li><li>Dutch Smoked</li><li>Goat Milk</li></ul>
  <ul class="list" style="left:161px;top:59px"><li>Mild Salsa</li><li>Spicy Salsa</li><li>Avocado</li><li>Hommus</li><li>Sweet Potato</li><li>Caramelised Onion</li><li>Roast Capsicum</li><li>Caviar</li><li>Guacamole</li><li>Sweet Chilli &amp; Sour Cream</li><li>Cashews</li><li>Jalapeno</li></ul>
  <div class="ribbon sm" style="left:11px;top:173px;width:97px">CRACKERS</div>
  <ul class="list" style="left:11px;top:200px"><li>Krisp</li><li>Natural Artisan Crackers</li><li>Wheatlies</li><li>Flat bread</li><li>Chilli jam flat bread</li><li>Assorted crackers</li><li>Veggie crackers</li></ul>
  <ul class="list" style="left:85px;top:200px"><li>Pita Crackers</li><li>Bread Sticks</li><li>Corntops</li><li>Bruschetta Toasts</li><li>Wafer Crackers</li><li>Ricey</li></ul>
  <div class="photo" role="img" aria-label="Wooden board with assorted crackers and soft cheeses" style="left:142px;top:182px;width:96px;height:155px;background:linear-gradient(135deg,#d9b27a,#e8cfa0 50%,#b88a52);border-radius:10px 0 0 0"></div>
  <div class="photo" role="img" aria-label="Two corn chips" style="left:64px;top:265px;width:40px;height:50px;background:linear-gradient(135deg,#f0cf7c,#d9a84f);border-radius:6px"></div>
  <div class="choose" style="left:136px;top:211px;width:32px;height:32px;font-size:7px">Choose<small>any 2</small></div>
</section>

<section class="page p3">
  <div class="ribbon sm" style="left:26px;top:14px;width:185px">COMPLIMENTARY BEVERAGES</div>
  <div class="photo" role="img" aria-label="Glass of red wine beside two wine bottles" style="left:15px;top:38px;width:80px;height:80px;background:linear-gradient(135deg,#efe9e6,#6a1620 55%,#2a1a16);border-radius:6px"></div>
  <div class="ribbon sm" style="left:108px;top:48px;width:74px">WINE</div>
  <div class="choose" style="left:195px;top:36px;width:32px;height:32px;font-size:7px">Choose<small>any 2</small></div>
  <ul class="list" style="left:109px;top:72px"><li>Champagne</li><li>Sauvignon Blanc</li><li>Chadonnay</li><li>Malbec</li></ul>
  <ul class="list" style="left:163px;top:72px"><li>Shiraz</li><li>Cabernet Sauvignon</li><li>Merlot</li></ul>
  <div class="ribbon sm" style="left:14px;top:125px;width:74px">BEER</div>
  <ul class="list" style="left:14px;top:150px"><li>Craft Lager</li><li>Craft Pale Ale</li><li>Craft XPA</li><li>Australian Lager</li></ul>
  <ul class="list" style="left:68px;top:150px"><li>Australian Dry</li><li>International Lager</li><li>Cider</li></ul>
  <div class="photo" role="img" aria-label="Mug and glass of golden beer" style="left:132px;top:105px;width:98px;height:76px;background:linear-gradient(135deg,#f3f1ec,#f0b21c 50%,#d98414);border-radius:6px"></div>
  <div class="ribbon sm" style="left:97px;top:189px;width:120px">NON ALCOHOLIC</div>
  <ul class="list" style="left:98px;top:212px"><li>Fizz Cola</li><li>Fizz No Sugar</li><li>Diet Fizz</li><li>Fizz Caffeine Free</li><li>Vanilla Fizz</li><li>Polar Cola</li><li>Polar Max</li><li>Polar Max Vanilla</li><li>Spritz Lemon Lime</li><li>Orangette</li></ul>
  <ul class="list" style="left:160px;top:212px"><li>Ridge Dew</li><li>Zest</li><li>Zest Zero Sugar</li><li>Sunbright</li><li>Sunbright Zero Sugar</li><li>Apple Cider</li><li>Ginger Beer</li><li>Diet Ginger Beer</li><li>Lemon Lime &amp; Bitters</li><li>Creaming Soda</li><li>Sugar Free Creaming Soda</li></ul>
  <div class="photo" role="img" aria-label="Glasses of colourful juice and soft drinks" style="left:0;top:205px;width:92px;height:85px;background:linear-gradient(90deg,#f6a27e,#f7b733 45%,#e8432e)"></div>
  <div class="ribbon sm" style="left:10px;top:309px;width:142px">WATER PREFERENCE</div>
  <ul class="list" style="left:161px;top:310px"><li>Still</li><li>Sparkling</li></ul>
  <ul class="list" style="left:194px;top:310px;line-height:6px"><li>Still &amp;<br>&nbsp;&nbsp;&nbsp;&nbsp;Sparkling</li></ul>
</section>

<section class="page p4">
  <div class="ribbon sm" style="left:10px;top:19px;width:75px">FRUIT</div>
  <ul class="list" style="left:11px;top:44px"><li>Strawberrys</li><li>Grapes</li><li>Passion Fruit</li></ul>
  <ul class="list" style="left:65px;top:44px"><li>Oranges</li><li>Kiwi Fruit</li></ul>
  <div class="photo" role="img" aria-label="Strawberries, green grapes, passion fruit, kiwi fruit and oranges" style="left:78px;top:64px;width:160px;height:116px;background:radial-gradient(circle at 30% 30%,#d8232a,transparent 40%),radial-gradient(circle at 75% 30%,#8cc63f,transparent 40%),radial-gradient(circle at 80% 75%,#f7941d,transparent 40%),linear-gradient(135deg,#6b2c3f,#8a6a3c);border-radius:30px 0 0 30px"></div>
  <div class="choose" style="left:55px;top:84px;width:32px;height:32px;font-size:7px">Choose<small>any 3</small></div>
  <div class="ribbon sm" style="left:114px;top:197px;width:107px">CHOCOLATES</div>
  <ul class="list" style="left:121px;top:221px"><li>Hazel Royale</li><li>Alpine Peaks</li><li>Velour Truffles</li><li>Rocky Road</li></ul>
  <ul class="list" style="left:174px;top:221px"><li>Crisp Bar</li><li>Malt Drops</li><li>Creamery Chocolate</li></ul>
  <div class="photo" role="img" aria-label="Box of gold-wrapped hazelnut chocolates" style="left:10px;top:210px;width:96px;height:92px;background:linear-gradient(135deg,#f3e3b0,#c99a3c 55%,#6b4020);border-radius:8px"></div>
  <div class="photo" role="img" aria-label="Bar of milk chocolate wafer fingers" style="left:152px;top:262px;width:60px;height:40px;background:linear-gradient(135deg,#8a5a44,#5a3424);border-radius:3px;transform:rotate(-15deg)"></div>
  <div class="choose" style="left:68px;top:206px;width:32px;height:32px;font-size:7px">Choose<small>any 1</small></div>
</section>

<div class="side-brand"><span class="dot"></span>Fernvale Hampers</div>

</body>
</html>
```